Harbor Leaf Salvage Centre

Text draft only
‘HELP! Stop toxic landfill pollution’
Australians are addicted to all forms new electronic equipment, we consume more per head of population than any country on the Planet!On average we now ditch a television each 2 years, we purchase the latest smart phone every year, the latest computer each year, SME’s and large corporation companies change IT hardware each 12 months. We purchased 17 million items new electronic purchases in 2011! The kicker is: (only 2.4 million) were correctly recycled.
If you are rolling over your IT Hardware, phones, or printers think first harbor Leaf Salvage, for a small fee we will correctly recycle your old E-Waste.
World standard ISO 14001.

‘TOGETHER WE CAN MAKE A DIFFERENCE’
THE NEW HARBOR LEAF SALVAGE CENTRE
47 Marlow St Kendrick
Opening hours: 8am – 4.pm Week days and 9am – midday Saturdays.
www.harborleafsalvage.example
1300 58 26 91

```html
<!DOCTYPE html>
<html lang="en">
<head>
<meta charset="utf-8">
<title>Harbor Leaf Salvage Centre – Stop toxic landfill pollution</title>
<link rel="stylesheet" href="https://fonts.googleapis.com/css2?family=Baloo+2:wght@600;700;800&family=Didact+Gothic&display=swap">
<style>
  :root {
    --backdrop: #d9d9d9;
    --paper: #c9e5bd;
    --green: #3f9a2a;
    --green-dark: #2f7d1f;
    --green-pale: #a9d39a;
    --sky-top: #2f7fc8;
    --sky-low: #9cc9ee;
    --grass: #4f9a2c;
    --ink: #1d1d1d;
    --white: #ffffff;
  }
  * { box-sizing: border-box; margin: 0; padding: 0; }
  html, body { width: 1200px; height: 900px; overflow: hidden; }
  body {
    background: var(--backdrop);
    position: relative;
    font-family: "Didact Gothic", "Helvetica Neue", Arial, sans-serif;
    color: var(--ink);
  }
  .flyer {
    position: absolute;
    left: 324px; top: 36px;
    width: 587px; height: 831px;
    background: var(--paper);
    border: 1px solid #444;
    box-shadow: 0 2px 8px rgba(0,0,0,.25);
    overflow: hidden;
  }
  .hero-photo {
    position: absolute; left: 0; top: 0;
    width: 100%; height: 420px;
    background: linear-gradient(180deg, var(--sky-top) 0%, var(--sky-low) 45%, #cfe6f5 58%, var(--grass) 72%, #2f6e1a 100%);
  }
  .headline-band {
    position: absolute; left: 0; top: 388px;
    width: 587px; height: 116px;
  }
  .help {
    position: absolute; left: 24px; top: 384px;
    font-family: "Baloo 2", "Arial Rounded MT Bold", sans-serif;
    font-weight: 800;
    font-size: 78px;
    line-height: 1;
    letter-spacing: 1px;
    color: var(--white);
    -webkit-text-stroke: 3px var(--green-dark);
    paint-order: stroke fill;
    text-shadow: 0 0 0 var(--white);
  }
  .slogan {
    position: absolute; right: 22px; top: 396px;
    text-align: right;
    font-family: "Baloo 2", "Arial Rounded MT Bold", sans-serif;
    font-weight: 700;
    color: var(--white);
    line-height: .95;
  }
  .slogan .big { display: block; font-size: 52px; }
  .slogan .small { display: block; font-size: 30px; margin-right: 50px; }
  .body-copy {
    position: absolute; left: 30px; top: 508px;
    width: 527px;
    text-align: center;
    font-size: 14px;
    line-height: 18.5px;
  }
  .body-copy p + p { margin-top: 16px; }
  .kicker { font-family: "Baloo 2", sans-serif; font-weight: 700; font-size: 14px; }
  .callout {
    position: absolute; left: 120px; top: 698px;
    width: 356px; height: 45px;
  }
  .callout-text {
    position: absolute; left: 120px; top: 700px;
    width: 356px;
    text-align: center;
    font-family: "Baloo 2", sans-serif;
    font-weight: 700;
    font-size: 13.5px;
    line-height: 19px;
    letter-spacing: .3px;
    color: var(--white);
  }
  .contact {
    position: absolute; left: 0; top: 752px;
    width: 100%;
    text-align: center;
    font-size: 13px;
    line-height: 18px;
  }
  .contact .web { font-family: "Baloo 2", sans-serif; font-weight: 700; }
</style>
</head>
<body>
  <main class="flyer">
    <div class="hero-photo" role="img" aria-label="Photo of a businessman in shirt and tie holding cash, standing in tall green grass under a blue sky, surrounded by floating bubbles containing a house, car, laptops, phone and charts"></div>

    <svg class="headline-band" viewBox="0 0 587 116" aria-hidden="true">
      <polygon points="0,104 587,104 587,116 0,116" fill="var(--green-pale)"/>
      <polygon points="0,0 260,0 260,92 0,92" fill="var(--green)"/>
      <polygon points="228,104 262,16 587,16 587,104" fill="var(--green)"/>
      <polygon points="0,92 262,92 258,104 0,104" fill="var(--green-pale)"/>
    </svg>

    <h1 class="help">HELP!</h1>
    <h2 class="slogan">
      <span class="big">stop toxic</span>
      <span class="small">landfill pollution</span>
    </h2>

    <section class="body-copy">
      <p>Australians are addicted to all forms new electronic equipment, we consume more per head of population than any country on the Planet!On average we now ditch a television each 2 years, we purchase the latest smart phone every year, the latest computer each year, SME’s and large corporation companies change IT hardware each 12 months. We purchased 17 million items new electronic purchases in 2011!<br><span class="kicker">The kicker is: (only 2.4 million) were correctly recycled.</span></p>
      <p>If you are rolling over your IT Hardware, phones, or printers think first harbor Leaf Salvage, for a small fee we will correctly recycle your old E-Waste.<br>World standard ISO 14001.</p>
    </section>

    <svg class="callout" viewBox="0 0 356 45" aria-hidden="true">
      <polygon points="18,0 356,0 338,45 0,45" fill="var(--green)"/>
    </svg>
    <p class="callout-text">TOGETHER WE CAN MAKE A DIFFERENCE<br>THE NEW HARBOR LEAF SALVAGE CENTRE</p>

    <address class="contact" style="font-style:normal">
      47 Marlow St Kendrick<br>
      Opening hours: 8am – 4.pm Week days and 9am – midday Saturdays.<br>
      <span class="web">www.harborleafsalvage.example</span><br>
      1300 58 26 91
    </address>
  </main>
</body>
</html>
```